RKW Automotive needs a catchy banner design

We need a design for a banner to be displayed on the fence in the outfield of a baseball stadium to show off our company and have people interested in what we do. We need something catchy that's going to attract people to look over at our banner.
We are a
Complete Automotive Service Company
Tires - Service - Repair - Diesel
We are in a Town called Maple-Hollow
(555)314-2096 we would like the phone number to be a descent size so when you are in the stands you can read it.
I have attached what we came up with but like I said we need it to pop more and make the viewer that's looking at it want to look us up.
The Banner size is 24ft long and 10ft tall

```html
<!DOCTYPE html>
<html lang="en">
<head>
<meta charset="utf-8">
<title>RKW Automotive – Outfield Banner</title>
<link rel="stylesheet" href="https://fonts.googleapis.com/css2?family=Exo+2:ital,wght@0,700;0,800;1,300;1,900&family=Saira+Condensed:wght@700&family=Questrial&display=swap">
<style>
  :root {
    --page-bg: #a9a9a9;
    --banner-dark: #0b0c12;
    --banner-mid: #1c2130;
    --brand-blue: #1f82ee;
    --brand-blue-deep: #0f5fcb;
    --brand-blue-light: #3aa2ff;
    --silver: #d9dadc;
    --white: #ffffff;
    --ink: #0a0a0a;
  }
  * { box-sizing: border-box; margin: 0; padding: 0; }
  html, body { width: 1126px; height: 1200px; overflow: hidden; }
  body {
    background: var(--page-bg);
    display: flex; align-items: center; justify-content: center;
  }
  .banner {
    position: relative;
    width: 1040px; height: 433px;
    overflow: hidden;
    background: radial-gradient(ellipse at 45% 40%, var(--banner-mid) 0%, var(--banner-dark) 75%);
  }
  .corner { position: absolute; inset: 0; width: 100%; height: 100%; }
  .brand-mark {
    position: absolute; left: 60px; top: 190px; width: 385px;
    display: flex; align-items: center; justify-content: center; gap: 14px;
    white-space: nowrap;
  }
  .brand-mark__dot {
    width: 30px; height: 30px; border-radius: 50%; flex: none;
    background: var(--brand-blue);
  }
  .brand-mark__name {
    font-family: "Exo 2", sans-serif; font-weight: 800;
    font-size: 40px; line-height: 1; color: var(--brand-blue); letter-spacing: 0.5px;
  }
  .headline { position: absolute; left: 470px; width: 520px; text-align: center; white-space: nowrap; }
  .headline--intro {
    top: 36px; font-family: "Exo 2", sans-serif; font-style: italic; font-weight: 300;
    font-size: 38px; color: var(--white); letter-spacing: -1.5px; padding-left: 40px;
  }
  .headline--main {
    top: 86px; font-family: "Exo 2", sans-serif; font-style: italic; font-weight: 900;
    font-size: 39px; color: var(--brand-blue); letter-spacing: -1px; text-transform: uppercase;
  }
  .headline--sub {
    top: 136px; font-family: "Exo 2", sans-serif; font-style: italic; font-weight: 900;
    font-size: 37px; color: var(--silver); letter-spacing: -0.5px; text-transform: uppercase;
    padding-right: 20px;
  }
  .services { position: absolute; left: 489px; top: 210px; width: 480px; height: 52px; }
  .services text {
    font-family: "Saira Condensed", sans-serif; font-weight: 700; font-style: italic;
    font-size: 30px; fill: var(--white); text-anchor: middle;
  }
  .location {
    position: absolute; left: 492px; top: 288px; white-space: nowrap;
    font-family: "Questrial", sans-serif; font-size: 22px; color: var(--white);
  }
  .location__town { color: var(--brand-blue-light); }
  .phone {
    position: absolute; left: 481px; top: 332px; width: 430px; height: 61px;
    border-radius: 31px; background: var(--white); white-space: nowrap;
    display: flex; align-items: center; gap: 14px; padding-left: 12px;
  }
  .phone__icon { width: 42px; height: 42px; flex: none; }
  .phone__number {
    font-family: "Exo 2", sans-serif; font-weight: 800; font-size: 44px; line-height: 1;
    color: var(--ink); letter-spacing: 1.5px;
  }
</style>
</head>
<body>
  <section class="banner" aria-label="RKW Automotive banner">
    <svg class="corner" viewBox="0 0 1040 433" preserveAspectRatio="none" aria-hidden="true">
      <defs>
        <linearGradient id="cornerBlue" x1="0" y1="0" x2="1" y2="1">
          <stop offset="0" stop-color="var(--brand-blue-deep)"/>
          <stop offset="1" stop-color="var(--brand-blue-light)"/>
        </linearGradient>
      </defs>
      <polygon points="0,0 88,0 0,215" fill="url(#cornerBlue)"/>
      <polygon points="1040,216 1040,433 950,433" fill="url(#cornerBlue)"/>
    </svg>

    <div class="brand-mark">
      <span class="brand-mark__dot"></span>
      <span class="brand-mark__name">RKW Automotive</span>
    </div>

    <p class="headline headline--intro">WE ARE A</p>
    <h1 class="headline headline--main">Complete Automotive</h1>
    <h2 class="headline headline--sub">Service Company</h2>

    <svg class="services" viewBox="0 0 480 52" aria-label="Tires, Service, Repair, Diesel">
      <defs>
        <linearGradient id="tagBlue" x1="0" y1="0" x2="0" y2="1">
          <stop offset="0" stop-color="var(--brand-blue-light)"/>
          <stop offset="1" stop-color="var(--brand-blue-deep)"/>
        </linearGradient>
      </defs>
      <g fill="url(#tagBlue)" stroke="#9fd0ff" stroke-width="0.8">
        <polygon points="0,0 88,0 100,26 88,52 0,52"/>
        <polygon points="91,0 219,0 231,26 219,52 91,52 103,26"/>
        <polygon points="222,0 336,0 348,26 336,52 222,52 234,26"/>
        <polygon points="339,0 468,0 480,26 468,52 339,52 351,26"/>
      </g>
      <text x="48" y="37">TIRES</text>
      <text x="164" y="37">SERVICE</text>
      <text x="288" y="37">REPAIR</text>
      <text x="410" y="37">DIESEL</text>
    </svg>

    <p class="location">We are in a Town called <span class="location__town">Maple-Hollow</span></p>

    <div class="phone">
      <svg class="phone__icon" viewBox="0 0 42 42" aria-hidden="true">
        <circle cx="21" cy="21" r="21" fill="var(--brand-blue)"/>
        <path d="M14 11c1-1 2.5-1 3.2 0l2.2 3.4c.6.9.4 2-.4 2.7l-1.5 1.2c1 2.4 2.8 4.3 5.2 5.4l1.3-1.5c.7-.8 1.900-.9 2.7-.3l3.3 2.3c1 .7 1 2.2 0 3.1l-1.6 1.5c-1.3 1.2-3.3 1.4-4.9.6C17.5 27 13.7 23 11.7 17.8c-.6-1.600-.2-3.4 1-4.6z" fill="var(--white)"/>
        <path d="M23 12a8 8 0 0 1 7 7M23 8a12 12 0 0 1 11 11" stroke="var(--white)" stroke-width="1.8" fill="none" stroke-linecap="round"/>
      </svg>
      <span class="phone__number">(555)314-2096</span>
    </div>
  </section>
</body>
</html>
```